Beer bottle label / Tap badge

What: Graphics to be used on both a beer tap badge and a beer bottle label
Requirements:
• Represent a differentiated quality product
• Include brewery name and logo for brand recognition
• Include and represent the Name “Idle Tide”
• Include the beer style “American Cream Ale”
• A format that can be used both in a circular tap badge and a square / rectangular bottle label
At Drifting Reed Brewing Co. we design and brew quality beers across a range of styles. We use traditional ingredients and techniques to produce brews for you that are bursting with flavor and easy to drink. Our passion and commitment to excellence are captured in every bottle. Give them a try and see what we mean.
Idle Tide
American Cream Ale
An easy drinking session beer that won’t make you work to enjoy it. This is crafted to be smooth with a modicum of honey toasted oats and a yeast strain that leaves a fruity, very light, soft balanced palate. Perfectly hopped for a balanced experience this beer is made for you.
Updates
Thanks to everyone who submitted a design. My apologies for not providing any feedback over the past few days since we took a short break over Christmas. We've extended the deadline by a few days and we'll be in touch shortly.
Industry/Entity Type
Brewery
Requirements
Must have
- - Include brewery name and logo for brand recognition
- Include and represent the Name “Idle Tide”
- Include the beer style “American Cream Ale”
- include volume (330ml) and % alcohol (4.5% alcohol)
Nice to have
- Idle Tide is a very drinkable, smooth and easy beer that is perfect for a sunny lazy afternoon. We would like the graphic to represent the beer. So, perhaps a friendly (smiling) skeleton on a hammock or on the beach enjoying life .....

```html
<!DOCTYPE html>
<html lang="en">
<head>
<meta charset="utf-8">
<title>Idle Tide – American Cream Ale Label</title>
<link href="https://fonts.googleapis.com/css2?family=Alfa+Slab+One&family=Rozha+One&family=Lobster&family=Open+Sans:wght@400&display=swap" rel="stylesheet">
<style>
  :root {
    --paper: #ffffff;
    --label-cream: #fdc96b;
    --rim-brown: #5a1612;
    --gold-light: #e6cf72;
    --gold-deep: #b8973a;
    --ink: #111111;
    --ribbon-dark: #560505;
    --ribbon-bright: #a30d0b;
    --ribbon-tail: #6d0a08;
    --title-tan: #a88546;
    --style-red: #8a1a0a;
    --seal-green: #4e6b2b;
    --wheat: #a0421b;
  }
  html, body {
    margin: 0;
    width: 1200px;
    height: 1025px;
    overflow: hidden;
    background: var(--paper);
  }
  .label { display: block; width: 1200px; height: 1025px; }
  .rim-outer { fill: var(--label-cream); stroke: var(--rim-brown); stroke-width: 8; }
  .rim-line { fill: none; stroke: var(--rim-brown); stroke-width: 2; }
  .rim-dash { fill: none; stroke: var(--rim-brown); stroke-width: 8; stroke-dasharray: 3 4; }
  .field { stroke: var(--rim-brown); stroke-width: 1.5; }
  .brand-mark { fill: var(--ink); }
  .brand-name {
    font-family: "Alfa Slab One", serif;
    fill: var(--ink);
    text-anchor: middle;
  }
  .ribbon-tail { fill: var(--ribbon-tail); }
  .beer-name {
    font-family: "Rozha One", serif;
    font-size: 108px;
    fill: var(--title-tan);
    text-anchor: middle;
  }
  .spec {
    font-family: "Open Sans", sans-serif;
    font-size: 24px;
    fill: var(--ink);
  }
  .seal-ring { fill: #ffffff; stroke: var(--seal-green); stroke-width: 10; stroke-dasharray: 3 2; }
  .seal-art { fill: var(--ribbon-tail); }
  .wheat-art { fill: var(--wheat); opacity: .85; }
  .beer-style {
    font-family: "Lobster", sans-serif;
    font-size: 36px;
    fill: var(--style-red);
  }
</style>
</head>
<body>
<svg class="label" viewBox="0 0 1200 1025" xmlns="http://www.w3.org/2000/svg">
  <defs>
    <radialGradient id="fieldGlow" cx="50%" cy="40%" r="65%">
      <stop offset="0%" stop-color="var(--gold-light)"/>
      <stop offset="100%" stop-color="var(--gold-deep)"/>
    </radialGradient>
    <linearGradient id="ribbonFill" x1="0" y1="0" x2="1" y2="0">
      <stop offset="0%" stop-color="var(--ribbon-dark)"/>
      <stop offset="100%" stop-color="var(--ribbon-bright)"/>
    </linearGradient>
    <path id="styleArc" d="M 420,905 Q 620,1010 830,895"/>
  </defs>

  <!-- label rim -->
  <ellipse class="rim-outer" cx="618" cy="513" rx="372" ry="507"/>
  <ellipse class="rim-line" cx="618" cy="513" rx="358" ry="493"/>
  <ellipse class="rim-dash" cx="618" cy="513" rx="350" ry="485"/>
  <ellipse class="rim-line" cx="618" cy="513" rx="342" ry="477"/>

  <!-- central field -->
  <ellipse class="field" cx="621" cy="510" rx="279" ry="425" fill="url(#fieldGlow)"
           role="img" aria-label="Warm golden sunburst texture"/>

  <!-- brewery name -->
  <circle class="brand-mark" cx="620" cy="190" r="42"/>
  <text class="brand-name" x="620" y="365" font-size="78">Drifting</text>
  <text class="brand-name" x="620" y="440" font-size="66">Reed</text>
  <text class="brand-name" x="620" y="505" font-size="40">Brewing Co.</text>

  <!-- ribbon -->
  <path class="ribbon-tail" d="M285,582 L305,575 L312,712 L292,715 Z"/>
  <path class="ribbon-tail" d="M920,560 L975,585 L970,740 L925,725 Z"/>
  <path d="M300,566 Q620,520 935,545 L935,712 Q620,688 310,675 Z" fill="url(#ribbonFill)"/>
  <text class="beer-name" x="615" y="665" transform="rotate(2.5 615 630)">Idle Tide</text>

  <!-- specs -->
  <text class="spec" x="396" y="727">volume (330ml)</text>
  <text class="spec" x="688" y="727">(4.5% alcohol)</text>

  <!-- seal with wheat -->
  <ellipse class="wheat-art" cx="490" cy="810" rx="20" ry="68" transform="rotate(-40 490 810)"
           role="img" aria-label="Wheat stalk"/>
  <ellipse class="wheat-art" cx="752" cy="810" rx="20" ry="68" transform="rotate(40 752 810)"
           role="img" aria-label="Wheat stalk"/>
  <circle class="seal-ring" cx="621" cy="833" r="76"/>
  <circle class="seal-art" cx="621" cy="833" r="56"
          role="img" aria-label="Three beer bottles above three stars"/>

  <!-- beer style -->
  <text class="beer-style"><textPath href="#styleArc" startOffset="50%" text-anchor="middle">American Cream Ale</textPath></text>
</svg>
</body>
</html>
```